Powerpoint design for european B2B business

We need a Powerpoint design for a newly established IT company with a B2B focus. We want to develop management information systems that help managers communicate goals into their organization and analyze their organizational activities and performance.

We defined the attached color scale, please relate your design to these colors.

The design should be simple and straight, serious and professional and leave enough space for the content ... :-)

Target Market(s)

B2B, companies larger than 200 employees

Industry/Entity Type

Business

Font styles to use
Sans Serif

Requirements
Should not have
• too playful design, clipart style

```html
<!DOCTYPE html>
<html lang="en">
<head>
<meta charset="utf-8">
<title>Veltaro – Presentation Template</title>
<link href="https://fonts.googleapis.com/css2?family=Open+Sans:wght@300;400;700&family=Carlito:wght@400;700&display=swap" rel="stylesheet">
<style>
  :root {
    --navy: #24496e;
    --navy-deep: #1d3d5f;
    --navy-light: #2f5a84;
    --green: #86c1a0;
    --text-grey: #5a5a5a;
    --text-dark: #333333;
    --backdrop: #c6c6c6;
    --paper: #ffffff;
  }
  * { margin: 0; padding: 0; box-sizing: border-box; }
  html, body { width: 900px; height: 1200px; overflow: hidden; }
  body {
    background: var(--backdrop);
    position: relative;
    font-family: "Carlito", "Open Sans", sans-serif;
  }
  .slide {
    position: absolute;
    width: 614px;
    height: 460px;
    background: var(--paper);
    box-shadow: 0 6px 18px rgba(0,0,0,0.22);
    overflow: hidden;
  }
  .slide--bar::after {
    content: "";
    position: absolute;
    left: 0; right: 0; bottom: 0;
    height: 5px;
    background: var(--navy);
  }

  /* Cover */
  .cover { left: 214px; top: 55px; z-index: 1; }
  .cover__backdrop {
    position: absolute; inset: 0;
    background: linear-gradient(160deg, var(--navy-light) 0%, var(--navy) 45%, var(--navy-deep) 100%);
  }
  .cover__title {
    position: absolute; left: 93px; top: 97px;
    font-family: "Open Sans", sans-serif;
    font-weight: 700;
    font-size: 41px;
    line-height: 37.5px;
    letter-spacing: -0.5px;
    color: var(--paper);
    text-transform: uppercase;
  }
  .cover__date {
    position: absolute; left: 93px; top: 272px;
    font-family: "Open Sans", sans-serif;
    font-weight: 300;
    font-size: 19px;
    color: #dfe7ef;
  }
  .brand {
    position: absolute;
    font-family: "Open Sans", sans-serif;
    font-weight: 700;
    letter-spacing: -1px;
    line-height: 1;
  }
  .cover .brand { left: 93px; top: 366px; font-size: 46px; color: var(--paper); }

  /* Content slides */
  .slide--back { left: 61px; top: 692px; z-index: 2; }
  .slide--front { left: 214px; top: 552px; z-index: 3; }
  .slide--back .brand,
  .slide--front .brand { left: 42px; top: 32px; font-size: 31px; color: var(--navy); }

  .intro {
    position: absolute; left: 0; right: 0; top: 128px;
    text-align: center;
    color: var(--navy);
    font-size: 15.5px;
    line-height: 23px;
  }
  .columns {
    position: absolute; left: 94px; top: 196px;
    display: flex; gap: 28px;
    height: 190px; overflow: hidden;
  }
  .columns p {
    width: 201px;
    font-size: 10.3px;
    line-height: 14.4px;
    color: var(--text-dark);
  }

  .lead {
    position: absolute; left: 0; right: 0; top: 87px;
    text-align: center;
  }
  .lead__heading {
    font-size: 19px; font-weight: 700;
    color: var(--green);
    letter-spacing: -0.3px;
    text-transform: uppercase;
  }
  .lead__text {
    margin-top: 6px;
    font-size: 16px; line-height: 23px;
    color: var(--navy);
  }
  .lead__rule {
    width: 65px; height: 1px;
    margin: 14px auto 0;
    background: var(--navy);
  }

  .stages { position: absolute; left: 114px; top: 196px; width: 440px; }
  .stage { display: flex; margin-bottom: 13px; }
  .stage__label {
    width: 92px;
    font-size: 16px; font-weight: 700;
    color: var(--navy);
    line-height: 22px;
  }
  .stage__title {
    font-size: 16px; font-weight: 700;
    color: var(--text-dark);
    line-height: 22px;
    letter-spacing: -0.2px;
  }
  .stage__points { list-style: none; margin-left: -12px; margin-top: 2px; }
  .stage__points li {
    display: flex; align-items: center; gap: 7px;
    font-size: 12.5px; line-height: 17px;
    color: var(--text-grey);
  }
  .stage__points svg { flex: none; }

  .corner-mark { position: absolute; }
  .slide--front .corner-mark { left: 565px; top: 483px; }
  .slide--back .corner-mark { left: 565px; top: 416px; }
</style>
</head>
<body>

  <section class="slide cover">
    <div class="cover__backdrop" role="img" aria-label="Blue-toned photograph of a modern glass office building seen from below"></div>
    <h1 class="cover__title">Lorem Ipsum<br>Presentations<br>and Annual<br>Reporting</h1>
    <p class="cover__date">JANUARY 2017</p>
    <div class="brand">Veltaro</div>
  </section>

  <section class="slide slide--bar slide--back">
    <div class="brand">Veltaro</div>
    <p class="intro">Maecenas molestie aliquam ligula euismod auctor.<br>Sed mi odio, blandit ut mi et, aliquet rutrum lorem.</p>
    <div class="columns">
      <p>Praesent laoreet nibh vel velit porttitor scelerisque. Phasellus at tortor ut ante quis convallis ornare. Donec eget scelerisque ligula, nec fermentum pellentesque in nulla. Integer vitae ipsum et lectus viverra augue. Ut suscipit nulla sit amet. Curabitur rutrum nisl a mauris rhoncus. Suspendisse potenti, quis dictum enim imperdiet a. Nullam lobortis augue mattis vehicula porta. Nullam in mauris in lorem pretium accumsan. Quisque laoreet ex neque, quis sagittis ex tincidunt vitae. Quisque felis nisi, commodo</p>
      <p>Praesent laoreet nibh vel velit porttitor scelerisque. Phasellus at tortor ut ante quis convallis ornare. Donec eget scelerisque ligula, nec fermentum pellentesque in nulla. Integer vitae ipsum et lectus viverra augue. Ut suscipit nulla sit amet. Curabitur rutrum nisl a mauris rhoncus. Suspendisse potenti, quis dictum enim imperdiet a. Nullam lobortis augue mattis vehicula porta. Nullam in mauris in lorem pretium accumsan. Quisque laoreet ex neque, quis sagittis ex tincidunt vitae. Quisque felis nisi, commodo</p>
    </div>
    <svg class="corner-mark" width="34" height="28" viewBox="0 0 34 28" aria-hidden="true">
      <rect x="12" y="6" width="22" height="22" fill="var(--green)"/>
    </svg>
  </section>

  <section class="slide slide--bar slide--front">
    <div class="brand">Veltaro</div>
    <div class="lead">
      <h2 class="lead__heading">Lorem ipsum dolor sit amet,</h2>
      <p class="lead__text">Maecenas molestie aliquam ligula euismod auctor.<br>Sed mi odio, blandit ut mi et, aliquet rutrum lorem.</p>
      <div class="lead__rule"></div>
    </div>

    <div class="stages">
      <div class="stage">
        <div class="stage__label">STAGE 1</div>
        <div>
          <div class="stage__title">Ut diam ante, dictum nec risus vitae,</div>
          <ul class="stage__points">
            <li><svg width="7" height="7" viewBox="0 0 7 7"><circle cx="3.5" cy="3.5" r="3" fill="none" stroke="var(--green)"/><circle cx="3.5" cy="3.5" r="1" fill="var(--green)"/></svg>in lacinia eros pharetra eget.</li>
            <li><svg width="7" height="7" viewBox="0 0 7 7"><circle cx="3.5" cy="3.5" r="3" fill="none" stroke="var(--green)"/><circle cx="3.5" cy="3.5" r="1" fill="var(--green)"/></svg>Praesent gravida diam ultricies faucibus</li>
          </ul>
        </div>
      </div>
      <div class="stage">
        <div class="stage__label">STAGE 2</div>
        <div>
          <div class="stage__title">Fact Finding and Trust Building (CS)</div>
          <ul class="stage__points">
            <li><svg width="7" height="7" viewBox="0 0 7 7"><circle cx="3.5" cy="3.5" r="3" fill="none" stroke="var(--green)"/><circle cx="3.5" cy="3.5" r="1" fill="var(--green)"/></svg>Vivamus tempor, tortor in malesuada</li>
            <li><svg width="7" height="7" viewBox="0 0 7 7"><circle cx="3.5" cy="3.5" r="3" fill="none" stroke="var(--green)"/><circle cx="3.5" cy="3.5" r="1" fill="var(--green)"/></svg>Pellentesque sagittis nulla</li>
          </ul>
        </div>
      </div>
      <div class="stage">
        <div class="stage__label">STAGE 3</div>
        <div>
          <div class="stage__title">Selling and Validating (SP)</div>
          <ul class="stage__points">
            <li><svg width="7" height="7" viewBox="0 0 7 7"><circle cx="3.5" cy="3.5" r="3" fill="none" stroke="var(--green)"/><circle cx="3.5" cy="3.5" r="1" fill="var(--green)"/></svg>Ut diam ante, dictum nec risus</li>
            <li><svg width="7" height="7" viewBox="0 0 7 7"><circle cx="3.5" cy="3.5" r="3" fill="none" stroke="var(--green)"/><circle cx="3.5" cy="3.5" r="1" fill="var(--green)"/></svg>Duis nec dolor suscipit, elementum</li>
          </ul>
        </div>
      </div>
    </div>

    <svg class="corner-mark" width="34" height="28" viewBox="0 0 34 28" aria-hidden="true">
      <rect x="12" y="6" width="22" height="22" fill="var(--green)"/>
    </svg>
  </section>

</body>
</html>
```